Medical Internet Marketing Company Needs a Site!

We need a new, fresh website for our search engine optimization and social media marketing company. We specialize in helping medical practices, doctors, physicians, and hospitals with their online presence and web ranking. The site should lean towards being suited for these audiences.

We have several examples of website that we like as well as things that we like about them.

Here are sites that we enjoy.

www.brightwavepromo.com

It's a good design for the site all around. The videos, buttons, and images are all excellent. They did a fine job.

- We really like their "contact us" side bar and want to include one like it on the secondary pages.

www.kestrelgrow.net

- We don't like the "thickness" of the top navigation bar.
- We like the page colors, easy navigation, and big call to action phone number in the top right corner.

http://www.tulavo.com/

Out of all the examples provided, Tulavo is our favorite and closest look and style to what we are looking for.

- We really like the openness of the design, such as space between the text and background.

- We want a price page in a style very similar to their pricing page with the services listed and check-marks, etc. although we intend to have multiple service package columns much like Kestrel's SEO pricing page.

- The way the video fits into the home page header is very organized, simple, and attention grabbing. We intend to place a slider with videos here.

- We need a page design that will allow for an image slider like Tulavo's Features page.

Here's a great example of a medical internet marketing website: http://www.dorvanta.com/

Target Market(s)

Our target market is doctors, typically male and typically 40-45 years old. I

Industry/Entity Type

Marketing

Requirements
Must have
• The homepage should have a slider in the video. Interior pages should have a video in the very top similar to how they do it on www.brightwavepromo.com

The top navigation tabs needed are:
- Home
- Solutions
- Resources
- About
- Why Zentrol
- Contact

The sidebar should have a GREAT call to action in it on interior pages.

There should be one interior page that is similar to this - http://www.tulavo.com/pricing/

There needs to be a page with multiple boxes that take up a row of the web page's body. This page will house all the case studies similar to brightwave promo's: http://www.brightwavepromo.com/success-stories/case-studies/ The one exception is we want the case studies to be inside of "boxes" instead of between horizontal lines like brightwave promo's.
Nice to have
• Color, professional, and clean. GREAT use of calls to actions.

```html
<!DOCTYPE html>
<html lang="en">
<head>
<meta charset="utf-8">
<title>Zentrol – Internet Marketing Planning</title>
<link rel="stylesheet" href="https://fonts.googleapis.com/css2?family=PT+Sans:ital,wght@0,400;0,700;1,400&family=PT+Sans+Narrow:wght@400;700&display=swap">
<style>
:root{
  --ink:#3a3a3a;
  --muted:#666;
  --topbar:#111;
  --header:#050505;
  --nav-text:#e6e6e6;
  --tab-top:#ffd95a;
  --tab-bottom:#f0b51e;
  --hero-light:#fff3a8;
  --hero-mid:#ffd63a;
  --hero-deep:#f6a609;
  --hero-title:#7a5a08;
  --hero-text:#8a6512;
  --orange:#f08a1a;
  --orange-dark:#c8620a;
  --page:#f7f7f7;
  --footer:#2b2b2b;
  --footer-text:#e5e5e5;
}
*{margin:0;padding:0;box-sizing:border-box}
html,body{width:800px;height:1200px;overflow:hidden}
body{position:relative;background:var(--page);font-family:"PT Sans",Arial,sans-serif;color:var(--ink)}
.abs{position:absolute}

/* top bar */
.topbar{left:0;top:0;width:800px;height:25px;background:var(--topbar)}
.phone-icon{left:566px;top:3px;width:19px;height:19px;background:#ddd;border-radius:3px}
.phone-call{left:591px;top:5px;color:#fff;font-size:12px;font-weight:700;white-space:nowrap}

/* header */
.site-header{left:0;top:25px;width:800px;height:55px;background:var(--header)}
.brand{left:87px;top:38px;display:flex;align-items:center;gap:10px}
.brand-square{width:26px;height:26px;background:var(--hero-mid)}
.brand-name{font-size:30px;color:#d9d9d9;letter-spacing:1px;font-weight:400}
.main-nav{left:0;top:25px;height:55px}
.main-nav a{position:absolute;top:0;height:55px;line-height:55px;color:var(--nav-text);font-size:10.5px;text-decoration:none;white-space:nowrap}
.main-nav a.active{background:linear-gradient(var(--tab-top),var(--tab-bottom));color:#3a2a00;font-weight:700;width:42px;text-align:center;font-size:11px}

/* hero */
.hero{left:0;top:80px;width:800px;height:274px;overflow:hidden;
  background:radial-gradient(ellipse 70% 90% at 25% 35%,var(--hero-light),var(--hero-mid) 60%,var(--hero-deep) 100%)}
.hero-wave{left:0;top:0}
.hero-title{left:87px;top:106px;font-family:"PT Sans Narrow","PT Sans",sans-serif;font-weight:700;font-size:25px;color:var(--hero-title);white-space:nowrap}
.hero-points{left:87px;top:156px;list-style:none;font-size:9.5px;color:var(--hero-text);line-height:16.5px;white-space:nowrap}
.hero-points li::before{content:"›";margin-right:5px;font-weight:700}
.hero-copy{left:87px;top:220px;width:280px;font-size:9px;line-height:16px;color:var(--hero-text);text-align:justify}
.signup{left:87px;top:303px;width:150px;height:34px;border-radius:5px;background:linear-gradient(#f7a23a,var(--orange-dark));display:flex;align-items:center;gap:8px;padding-left:5px;box-shadow:0 2px 3px rgba(0,0,0,.25)}
.signup-icon{width:34px;height:28px}
.signup span{color:#fff;font-size:15px;font-family:"PT Sans Narrow","PT Sans",sans-serif}
.showcase{left:375px;top:110px;width:329px;height:265px;border-radius:8px;
  background:linear-gradient(180deg,#3a2b3e 0%,#8a3b3a 35%,#d9a060 65%,#c9c9c9 80%,#9a9a9a 100%)}

/* welcome */
.section-title{font-family:"PT Sans",sans-serif;font-size:20px;font-weight:400;color:#444;white-space:nowrap}
.section-title b{font-weight:700}
.welcome-title{left:87px;top:404px}
.welcome-list{left:87px;top:443px;width:362px;list-style:none;font-size:8.3px;line-height:16.8px;color:var(--muted)}
.welcome-list li{padding-left:23px;position:relative}
.welcome-list li::before{content:"";position:absolute;left:0;top:4px;width:10px;height:8px;background:var(--orange)}
.read-more-link{left:87px;top:702px;font-size:9px;color:var(--muted);text-decoration:underline}

.testimonials-title{left:475px;top:404px}
.testimonial{left:477px;top:445px;width:227px;font-size:8.8px;line-height:15px;font-style:italic;color:var(--muted)}
.testimonial-author{left:477px;top:511px;width:224px;text-align:right;font-size:8.5px;font-weight:700;color:#333}
.slider-dots{left:677px;top:528px;display:flex;gap:2px}
.slider-dots i{width:5px;height:5px;background:#aaa}
.slider-dots i.on{background:var(--orange)}
.videos-title{left:475px;top:541px}
.video-still{left:478px;top:579px;width:224px;height:125px;
  background:linear-gradient(135deg,#c9a98a 0%,#8ea07a 45%,#5e6e5a 100%)}

/* services */
.services-title{left:87px;top:756px}
.service{top:802px;width:138px}
.service h3{font-size:10.5px;font-weight:400;color:#333;text-transform:uppercase;margin-bottom:6px;white-space:nowrap}
.service-image{width:138px;height:69px;border:1px solid #ddd}
.service p{font-family:Arial,sans-serif;font-size:8px;line-height:12.6px;color:var(--muted);margin-top:14px;text-align:justify}
.btn-more{display:block;width:48px;height:18px;margin-top:4px;border:1px solid #ccc;border-radius:2px;background:linear-gradient(#fff,#e4e4e4);font-size:6.5px;line-height:16px;text-align:center;color:#555}

/* footer */
.site-footer{left:0;top:1008px;width:800px;height:192px;background:var(--footer)}
.footer-col{top:1022px;color:var(--footer-text)}
.footer-col h4{font-size:13px;font-weight:400;margin-bottom:5px;white-space:nowrap}
.footer-col ul{list-style:none;font-size:8px;line-height:13.7px}
.social{display:flex;gap:5px;margin-top:6px}
.social i{width:21px;height:21px;border-radius:50%;background:#6a6a6a}
.social i.on{background:#5aa6d6}
.news-form input,.news-form textarea{display:block;width:137px;border:0;background:#fff;font-family:Arial,sans-serif;font-size:7px;padding:3px 4px;margin-bottom:3px;resize:none}
.news-form input{height:15px}
.news-form textarea{height:45px}
.subscribe{left:650px;top:1136px;width:54px;height:16px;border-radius:2px;background:linear-gradient(#555,#111);color:#fff;font-size:9px;text-align:center;line-height:16px}
.copyright{left:0;top:1181px;width:800px;text-align:center;color:#ccc;font-size:8px}
</style>
</head>
<body>

<div class="abs topbar"></div>
<div class="abs phone-icon">
  <svg width="19" height="19" viewBox="0 0 19 19"><path d="M6 4c1 0 2 2 2 3s-1 1-1 2 2 3 3 3 1-1 2-1 3 1 3 2-1 2-2 2c-4 0-9-5-9-9 0-1 1-2 2-2z" fill="#222"/></svg>
</div>
<div class="abs phone-call">Call us on: 555-014-2290</div>

<header class="abs site-header"></header>
<div class="abs brand"><span class="brand-square"></span><span class="brand-name">ZENTROL</span></div>
<nav class="abs main-nav">
  <a class="active" style="left:382px">Home</a>
  <a style="left:435px">Solutions</a>
  <a style="left:496px">Resources</a>
  <a style="left:559px">About</a>
  <a style="left:604px">Why Zentrol</a>
  <a style="left:673px">Contact</a>
</nav>

<section class="abs hero">
  <svg class="abs hero-wave" width="800" height="274" viewBox="0 0 800 274">
    <path d="M0 200 C200 150 400 240 800 160 L800 274 L0 274Z" fill="#f5a70b" opacity=".55"/>
    <path d="M0 240 C250 190 500 260 800 210 L800 274 L0 274Z" fill="#f19a05" opacity=".6"/>
  </svg>
</section>
<h1 class="abs hero-title">Internet Marketing Planning</h1>
<ul class="abs hero-points">
  <li>Proven to help grow medical practices — 6,000+ satisfied clients</li>
  <li>Websites, mobile sites, local search and more...</li>
  <li>Fast, easy and affordable</li>
</ul>
<p class="abs hero-copy">ZENTROL is a national, medical Internet-marketing group.We empower doctors nationwide by building their practices with highly specialized engagement strategies designed to bring in real patients.</p>
<a class="abs signup">
  <svg class="signup-icon" viewBox="0 0 34 28"><circle cx="17" cy="14" r="13" fill="#fff"/><path d="M13 5h8v9h5l-9 10-9-10h5z" fill="#2a8ad0"/></svg>
  <span>Sign up for free</span>
</a>
<div class="abs showcase" role="img" aria-label="Desktop monitor showing a video player with a colourful abstract still"></div>

<h2 class="abs section-title welcome-title">Welcome to <b>ZENTROL</b> Website</h2>
<ul class="abs welcome-list">
  <li>We are a GROUP: dispels the possible perception of being a one-man show andconveys intimacy, specialization and collaboration (vs. company, agency or firm).</li>
  <li>We EMPOWER doctors nationwide: immediately describes core audience and sizeof market, plus, the word "empower" elevates ZENTROL as the authority on medical Internet marketing vs. being perceived as a mere provider.</li>
  <li>We BUILD their practices: implies an immediate and specific benefit and purposeluses the word "build" to complement the ZENTROL name.</li>
  <li>Highly specialized PATIENT-ENGAGEMENT strategies: Patient engagement is hugefor ZENTROL -- its "spine," if you will, that is supported by ZENTROL'S results-focusedSEO and outstanding social media services.</li>
  <li>Designed to bring in REAL PATIENTS: This is ZENTROL's key differentiator.ZENTROL knows that its medical clients aren't just satisfied with anyone visiting their medical websites. They want the right someone so their practice can be successful. Also note the wording "designed to" -- which promises intent but is not a guarantee. Just a safeguard.</li>
  <li>ZENTROL is the medical industry's SEO specialist, unlike its "general practitioner" competitors.</li>
</ul>
<a class="abs read-more-link">Read more</a>

<h2 class="abs section-title testimonials-title">Client <b>Testimonials</b></h2>
<p class="abs testimonial">"Placerat sit amet leo. Vestibulum rutrum risus vel enim tincidunt a sagittis velit vehicula. Vestibulum ante ipsum primis in faucibus orci luctus et ultrices posuere cubilia Curae.Quisque elementum venenatis libero."</p>
<p class="abs testimonial-author">Daniel Mercer, Ceo Northgate Telecom</p>
<div class="abs slider-dots"><i class="on"></i><i class="on"></i><i></i><i></i></div>
<h2 class="abs section-title videos-title">See <b>Videos</b></h2>
<div class="abs video-still" role="img" aria-label="Video still of a businessman seated outdoors, with playback controls"></div>

<h2 class="abs section-title services-title">Medical Website <b>Services</b></h2>
<article class="abs service" style="left:87px">
  <h3>Mobile Websites</h3>
  <div class="service-image" role="img" aria-label="Smartphones and tablets" style="background:linear-gradient(135deg,#e8e8e8,#6a6a6a)"></div>
  <p>Lorem Ipsum is simply dummy text of the printing and typesetting industry. Lorem Ipsum has been the industry's.</p>
  <span class="btn-more">Read more</span>
</article>
<article class="abs service" style="left:246px">
  <h3>Patients Education</h3>
  <div class="service-image" role="img" aria-label="Doctor talking with a patient" style="background:linear-gradient(135deg,#5a3a3a,#d8cfc8)"></div>
  <p>Lorem Ipsum is simply dummy text of the printing and typesetting industry. Lorem Ipsum has been the industry's.</p>
  <span class="btn-more">Read more</span>
</article>
<article class="abs service" style="left:406px">
  <h3>Social &amp; Media Blogs</h3>
  <div class="service-image" role="img" aria-label="Network of social media icons" style="background:linear-gradient(135deg,#f4f4f4,#b8c8dc)"></div>
  <p>Lorem Ipsum is simply dummy text of the printing and typesetting industry. Lorem Ipsum has been the industry's.</p>
  <span class="btn-more">Read more</span>
</article>
<article class="abs service" style="left:565px">
  <h3>Doctor's Portal</h3>
  <div class="service-image" role="img" aria-label="Portrait of a doctor in a hospital corridor" style="background:linear-gradient(135deg,#dfeff0,#c8b8a8)"></div>
  <p>Lorem Ipsum is simply dummy text of the printing and typesetting industry. Lorem Ipsum has been the industry's.</p>
  <span class="btn-more">Read more</span>
</article>

<footer class="abs site-footer"></footer>
<div class="abs footer-col" style="left:87px">
  <h4>Main Links</h4>
  <ul><li>Home</li><li>Solutions</li><li>Resources</li><li>About</li><li>Why Zentrol</li><li>Contact</li></ul>
</div>
<div class="abs footer-col" style="left:246px">
  <h4>Follow us on</h4>
  <div class="social"><i></i><i class="on"></i><i></i><i></i></div>
</div>
<div class="abs footer-col" style="left:406px">
  <h4>Other Links</h4>
  <ul><li>Contact Us</li><li>Terms &amp; Conditions</li><li>Privacy Policy</li><li>Legal Disclosure</li><li>User Agreement</li></ul>
</div>
<div class="abs footer-col news-form" style="left:566px">
  <h4>Get News Updates</h4>
  <input placeholder="Name:">
  <input placeholder="Email:">
  <textarea placeholder="Message:"></textarea>
</div>
<div class="abs subscribe">Subscribe</div>
<p class="abs copyright">© 2012 Zentrol Website.All Rights Reserved</p>

</body>
</html>
```